website design for Company MVR

Our company name MVR(the grand mural limited), need design a website. It is a website that focuses on promoting art design in the world.
We will provide the existing logo design, the new website and logo should be matched to each other. The website has to include pages "Home" "Contact" "Service" and So on at least 6-8 pages. The site is mainly for publicity and promotion. We will have an existing domain and hosting.
Updates

We prefer the original design, thanks.

Target Market(s)

large public art

Industry/Entity Type

Architecture and design, large public art and sculpture manufacturer

Coding

Coded - Design and coding required

Number of Pages Required

5+ page

Requirements
Must have
• 1. the overall color has to match our logo color 2. Do not need to do any change on our logo including the color 3. Here is a similar style of the home page we like, it can be similar but must not same. Pls check the below link. https://www.velmardo.it/en-us/

```html
<!DOCTYPE html>
<html lang="en">
<head>
<meta charset="utf-8">
<title>MVR – The Grand Mural Limited</title>
<link href="https://fonts.googleapis.com/css2?family=Questrial&family=Arimo:wght@400;700&display=swap" rel="stylesheet">
<style>
:root{
  --ink:#2a2a2a;
  --ink-soft:#4a4a4a;
  --text:#555555;
  --cream:#eeeee1;
  --cream-dark:#e6e6d8;
  --white:#ffffff;
  --footer:#2b2b2b;
  --star:#e8871e;
  --field-line:#c9c9bd;
}
*{box-sizing:border-box;margin:0;padding:0}
html,body{width:1200px;height:4138px;overflow:hidden}
body{font-family:"Arimo",Arial,sans-serif;color:var(--ink);background:var(--white);position:relative}
.display{font-family:"Questrial",Arial,sans-serif;text-transform:uppercase;letter-spacing:.02em}
section,header,footer{position:absolute;left:0;width:1200px}
.abs{position:absolute}

/* header */
.site-header{top:0;height:146px;background:var(--white)}
.brand{left:111px;top:48px;display:flex;align-items:center;gap:14px}
.brand-name{font-family:"Questrial",sans-serif;font-size:40px;color:var(--ink);letter-spacing:.02em}
.brand-sub{font-family:"Questrial",sans-serif;font-size:20px;line-height:22px;color:var(--ink-soft);text-transform:uppercase;letter-spacing:.12em}
.main-nav{right:112px;top:64px;display:flex;gap:41px}
.main-nav a{font-family:"Questrial",sans-serif;font-size:16px;color:var(--ink);text-decoration:none;text-transform:uppercase}

/* hero */
.hero{top:146px;height:692px;background:radial-gradient(ellipse at 50% 45%,#6a6570 0%,#3d3a44 45%,#2a2630 100%)}
.hero-floor{left:0;bottom:0;width:1200px;height:230px;background:linear-gradient(#4a3a30,#2e241e)}
.hero-title{left:0;width:1200px;top:214px;text-align:center;font-size:54px;color:var(--white)}
.hero-sub{left:0;width:1200px;top:298px;text-align:center;font-size:22px;line-height:33px;color:var(--white)}
.btn-ghost{border:2px solid var(--white);border-radius:30px;color:var(--white);font-family:"Questrial",sans-serif;font-size:16px;text-transform:uppercase;display:flex;align-items:center;justify-content:center}

/* welcome */
.welcome{top:838px;height:658px;background:var(--cream)}
.eyebrow{left:111px;top:155px;font-size:20px;color:var(--ink-soft)}
.welcome-title{left:111px;top:182px;font-size:30px;color:var(--ink)}
.welcome-text{left:111px;top:244px;width:437px;font-size:13px;line-height:26.5px;color:var(--text);text-align:justify}
.btn-dark{background:var(--ink);color:var(--white);border-radius:30px;font-family:"Questrial",sans-serif;font-size:16px;text-transform:uppercase;display:flex;align-items:center;justify-content:center}
.photo-large{left:683px;top:57px;width:405px;height:485px;background:linear-gradient(135deg,#c8482c 0%,#3f6f8e 45%,#2f3c54 100%)}
.photo-small{left:618px;top:278px;width:287px;height:317px;border:5px solid var(--white);background:linear-gradient(160deg,#27384a,#1a2330 60%,#3a2a2a)}

/* section headings */
.section-title{left:0;width:1200px;text-align:center;font-size:28px;color:var(--ink)}
.section-sub{left:0;width:1200px;text-align:center;font-size:14px;color:var(--text)}

/* services */
.services{top:1496px;height:727px;background:var(--white)}
.service-card{top:179px;width:310px;height:397px}
.service-photo{left:0;top:0;width:310px;height:339px}
.service-edge{right:0;top:339px;width:25px;height:58px;background:#5a4a3e}
.service-name{left:15px;top:338px;font-size:20px;color:var(--ink)}
.service-text{left:16px;top:377px;width:250px;font-size:12.5px;line-height:25px;color:var(--text)}
.service-more{left:16px;top:438px;font-family:"Questrial",sans-serif;font-size:14px;color:var(--ink-soft);text-transform:uppercase}

/* banner */
.banner{top:2223px;height:530px;background:radial-gradient(ellipse at 50% 30%,#6a6d78 0%,#454650 50%,#2e2b2e 100%)}
.banner-floor{left:0;bottom:0;width:1200px;height:200px;background:linear-gradient(#6a3a26,#3a1e14)}
.banner-title{left:0;width:1200px;top:266px;text-align:center;font-size:44px;color:var(--white)}
.banner-text{left:0;width:1200px;top:328px;text-align:center;font-size:17px;line-height:31px;color:var(--white)}

/* products */
.products{top:2753px;height:550px;background:var(--white)}
.product{top:170px;width:233px;text-align:center}
.product-photo{width:233px;height:222px;box-shadow:0 2px 6px rgba(0,0,0,.25)}
.stars{margin-top:26px;color:var(--star);font-size:13px;letter-spacing:1px}
.product-name{margin-top:8px;font-family:"Questrial",sans-serif;font-size:18px;text-transform:uppercase;color:var(--ink-soft)}
.product-price{margin-top:8px;font-family:"Questrial",sans-serif;font-size:18px;color:var(--ink-soft)}

/* contact */
.contact{top:3303px;height:520px;background:linear-gradient(90deg,#e4e4d6,#ecebdf 50%,#e2e1d3)}
.field{background:rgba(255,255,255,.35);border:1px solid var(--field-line);font-size:13px;color:var(--ink-soft);padding:15px 19px}

/* footer */
.site-footer{top:3823px;height:315px;background:var(--footer);color:var(--white)}
.footer-brand{left:0;width:1200px;top:46px;display:flex;justify-content:center;align-items:center;gap:16px}
.footer-brand .brand-name,.footer-brand .brand-sub{color:var(--white)}
.footer-nav{left:0;width:1200px;top:138px;display:flex;justify-content:center;gap:58px}
.footer-nav a{font-family:"Questrial",sans-serif;font-size:16px;color:var(--white);text-decoration:none;text-transform:uppercase}
.social{left:0;width:1200px;top:185px;display:flex;justify-content:center;gap:9px}
.social span{width:34px;height:34px;border:1.5px solid var(--white);border-radius:50%}
.copyright{left:0;width:1200px;top:244px;text-align:center;font-size:14px}
</style>
</head>
<body>

<header class="site-header">
  <div class="abs brand">
    <span class="brand-name">MVR</span>
    <span class="brand-sub">The<br>Grand Mural</span>
  </div>
  <nav class="abs main-nav">
    <a href="#">Home</a><a href="#">Services</a><a href="#">Product</a><a href="#">Contact Us</a>
  </nav>
</header>

<section class="hero" role="img" aria-label="Photo of a classic art gallery hall with framed paintings and a skylit ceiling">
  <div class="abs hero-floor"></div>
  <h1 class="abs hero-title display">The Grand Mural</h1>
  <p class="abs hero-sub display">Sed ut perspiciatis unde omnis iste natus<br>error sit voluptatem</p>
  <a class="abs btn-ghost" style="left:514px;top:384px;width:172px;height:58px">Read More</a>
</section>

<section class="welcome">
  <p class="abs eyebrow display">Welcome to</p>
  <h2 class="abs welcome-title display">The Grand Mural Limited</h2>
  <p class="abs welcome-text">Sed ut perspiciatis unde omnis iste natus error sit voluptatem accus antium doloremque laudantium, totam rem aperiam, eaque ipsa quae ab illo inventore veritatis et quasi architecto beatae vitae dicta sunt explicabo. Nemo enim ipsam voluptatem quia voluptas sit aspernatur aut odit aut fugit, sed quia consequuntur magni dolores eos qui ratione natus error sit voluptatem sequi nesciunt.</p>
  <a class="abs btn-dark" style="left:112px;top:436px;width:161px;height:51px">Read More</a>
  <div class="abs photo-large" role="img" aria-label="Photo of an artist painting a colourful large-scale mural"></div>
  <div class="abs photo-small" role="img" aria-label="Photo of visitors viewing paintings in a dark gallery room"></div>
</section>

<section class="services">
  <h2 class="abs section-title display" style="top:52px">Our Services</h2>
  <p class="abs section-sub" style="top:105px">Sed ut perspiciatis unde omnis iste natus error sit voluptatem accusantium doloremque laudantium</p>

  <article class="abs service-card" style="left:111px">
    <div class="abs service-photo" role="img" aria-label="Photo of a visitor looking at large colourful paintings" style="background:linear-gradient(135deg,#4f8a73,#c9b866 50%,#7a3a28)"></div>
    <div class="abs service-edge"></div>
    <h3 class="abs service-name display">Services 01</h3>
    <p class="abs service-text">Nemo enim ipsam voluptatem quia volu ptas sit aspernatur aut odit aut</p>
    <a class="abs service-more">Read More</a>
  </article>
  <article class="abs service-card" style="left:445px">
    <div class="abs service-photo" role="img" aria-label="Photo of a bright exhibition hall with visitors" style="background:linear-gradient(180deg,#6a5a42,#d8cdb4 45%,#b19a78)"></div>
    <div class="abs service-edge"></div>
    <h3 class="abs service-name display">Services 02</h3>
    <p class="abs service-text">Nemo enim ipsam voluptatem quia volu ptas sit aspernatur aut odit aut</p>
    <a class="abs service-more">Read More</a>
  </article>
  <article class="abs service-card" style="left:779px">
    <div class="abs service-photo" role="img" aria-label="Photo of visitors in front of a vivid abstract painting" style="background:linear-gradient(135deg,#d6a21e,#e7d04a 45%,#3a2a22)"></div>
    <div class="abs service-edge"></div>
    <h3 class="abs service-name display">Services 03</h3>
    <p class="abs service-text">Nemo enim ipsam voluptatem quia volu ptas sit aspernatur aut odit aut</p>
    <a class="abs service-more">Read More</a>
  </article>
</section>

<section class="banner" role="img" aria-label="Photo of a museum gallery with visitors and a polished wooden floor">
  <div class="abs banner-floor"></div>
  <h2 class="abs banner-title display">The Grand Mural Limited</h2>
  <p class="abs banner-text">Sed ut perspiciatis unde omnis iste natus error sit voluptatem accusantium doloremque<br>laudantium, totam rem aperiam &nbsp;eaque ipsa quae</p>
  <a class="abs btn-ghost" style="left:517px;top:411px;width:166px;height:48px">Read More</a>
</section>

<section class="products">
  <h2 class="abs section-title display" style="top:58px">Our Product</h2>
  <p class="abs section-sub" style="top:112px">Sed ut perspiciatis unde omnis iste natus error sit voluptatem accusantium doloremque laudantium</p>

  <div class="abs product" style="left:111px">
    <div class="product-photo" role="img" aria-label="Painting of people with colourful umbrellas in the rain" style="background:linear-gradient(135deg,#e0a51c,#c8402e 50%,#3a6a8a)"></div>
    <div class="stars">★★★★★</div><div class="product-name">Product Name</div><div class="product-price">$25.00</div>
  </div>
  <div class="abs product" style="left:358px">
    <div class="product-photo" role="img" aria-label="Painting of sailing ships in a golden sunset harbour" style="background:linear-gradient(180deg,#f2d23a,#e88a2a 55%,#c24a2a)"></div>
    <div class="stars">★★★★★</div><div class="product-name">Product Name</div><div class="product-price">$25.00</div>
  </div>
  <div class="abs product" style="left:607px">
    <div class="product-photo" role="img" aria-label="Colourful abstract painting of an eye" style="background:linear-gradient(135deg,#d8432e,#3a9ac8 50%,#e6c02a)"></div>
    <div class="stars">★★★★★</div><div class="product-name">Product Name</div><div class="product-price">$25.00</div>
  </div>
  <div class="abs product" style="left:855px">
    <div class="product-photo" role="img" aria-label="Abstract painting of a city skyline reflected in water" style="background:linear-gradient(180deg,#d8d4cc,#8a8a92 55%,#c2543a)"></div>
    <div class="stars">★★★★★</div><div class="product-name">Product Name</div><div class="product-price">$25.00</div>
  </div>
</section>

<section class="contact">
  <h2 class="abs section-title display" style="top:57px">Contact Us</h2>
  <p class="abs section-sub" style="top:110px">Sed ut perspiciatis unde omnis iste natus error sit voluptatem accusantium doloremque</p>
  <div class="abs field" style="left:279px;top:161px;width:314px;height:47px">First Name :</div>
  <div class="abs field" style="left:606px;top:161px;width:313px;height:47px">Last Name :</div>
  <div class="abs field" style="left:279px;top:226px;width:314px;height:46px">Email :</div>
  <div class="abs field" style="left:606px;top:226px;width:313px;height:46px">Phone :</div>
  <div class="abs field" style="left:279px;top:290px;width:640px;height:98px">Message :</div>
  <a class="abs btn-dark" style="left:519px;top:414px;width:162px;height:50px">Submit</a>
</section>

<footer class="site-footer">
  <div class="abs footer-brand">
    <span class="brand-name" style="font-size:52px">MVR</span>
    <span class="brand-sub" style="font-size:26px;line-height:28px">The<br>Grand Mural</span>
  </div>
  <nav class="abs footer-nav">
    <a href="#">Home</a><a href="#">Services</a><a href="#">Product</a><a href="#">Contact Us</a>
  </nav>
  <div class="abs social"><span></span><span></span><span></span><span></span><span></span></div>
  <p class="abs copyright">© Copyright 2021The Grand Mural Limited.All Rights Reserved</p>
</footer>

</body>
</html>
```